Attractive Wall Posters wanted

We are designing posters for our outdoor wall to represent our brands.

(Portrait Layout: Measurements - Height 128cm, Width 108cm).

More information for each brand can be found on the website listed in the ppt attached.

Requirements
Must have
• The information included in PPT, the logo, the website and the short description
Nice to have
• Consistency across all posters
Should not have
• too cluttered designs

```html
<!DOCTYPE html>
<html lang="en">
<head>
<meta charset="utf-8">
<title>Learn – Wall Poster</title>
<link href="https://fonts.googleapis.com/css2?family=Bodoni+Moda:opsz,wght@6..96,400;6..96,600&display=swap" rel="stylesheet">
<style>
  :root {
    --navy-light: #1d2c72;
    --navy-mid: #141e58;
    --navy-dark: #0a0e3c;
    --red: #e0101f;
    --white: #ffffff;
    --paper: #ffffff;
    --frame: #8a8a8a;
    --green: #3aa142;
    --orange: #e46a3a;
    --magenta: #d0245a;
    --brand-dark: #1e2348;
  }
  html, body { margin: 0; padding: 0; overflow: hidden; background: var(--paper); }
  .poster {
    position: relative;
    width: 1011px; height: 1200px;
    background: var(--paper);
    box-sizing: border-box;
    border: 2px solid var(--frame);
    overflow: hidden;
    font-family: "Bodoni Moda", "Didot", serif;
  }
  .hero {
    position: absolute; left: 13px; top: 13px;
    width: 983px; height: 1029px;
    background: radial-gradient(ellipse 60% 55% at 48% 52%, var(--navy-light) 0%, var(--navy-mid) 55%, var(--navy-dark) 100%);
  }
  .word { position: absolute; margin: 0; line-height: 1; color: var(--white); white-space: nowrap; font-weight: 400; }
  .word--find { font-size: 166px; left: 431px; top: 236px; }
  .word--learn { color: var(--red); font-size: 219px; left: 215px; top: 324px; letter-spacing: -4px; }
  .word--start { font-size: 122px; left: 205px; top: 497px; letter-spacing: -1px; }
  .word--consultancy { font-size: 43px; left: 544px; top: 527px; }
  .vertical { writing-mode: vertical-rl; }
  .word--need { font-size: 52px; left: 480px; top: 540px; }
  .word--team { font-size: 54px; left: 810px; top: 180px; }
  .word--better { font-size: 66px; left: 136px; top: 270px; }
  .icon { position: absolute; width: 30px; height: 30px; }
  .footer { position: absolute; left: 0; top: 1042px; width: 100%; height: 140px; }
  .brand {
    position: absolute; top: 54px;
    display: flex; align-items: center; gap: 8px;
    font-family: "Bodoni Moda", "Didot", serif; font-weight: 600;
    font-size: 22px; line-height: 1; color: var(--brand-dark); white-space: nowrap;
  }
  .brand__dot { width: 22px; height: 22px; border-radius: 50%; background: var(--brand-dark); }
  .brand--reef { left: 66px; }
  .brand--study { left: 246px; }
  .brand--skill { left: 470px; }
  .brand--kvr { left: 722px; }
  .brand--north { left: 826px; font-size: 18px; }
</style>
</head>
<body>
<main class="poster">
  <section class="hero">
    <p class="word word--find">Find</p>
    <p class="word word--learn">Learn</p>
    <p class="word word--start">start</p>
    <p class="word word--consultancy">consultancy</p>
    <p class="word word--need vertical">need training</p>
    <p class="word word--team vertical">teambuilding</p>
    <p class="word word--better vertical">be better</p>

    <svg class="icon" style="left:151px;top:234px" viewBox="0 0 24 24" fill="var(--green)"><rect x="11" y="4" width="2" height="18"/><path d="M12 8 6 4v5l6 4zM12 8l6-4v5l-6 4zM12 14l-6-4v5l6 4zM12 14l6-4v5l-6 4z"/></svg>
    <svg class="icon" style="left:236px;top:301px" viewBox="0 0 24 24" fill="var(--white)"><circle cx="12" cy="10" r="7"/><rect x="9" y="17" width="6" height="4"/></svg>
    <svg class="icon" style="left:451px;top:226px" viewBox="0 0 24 24" fill="var(--white)"><circle cx="10" cy="7" r="5"/><path d="M1 22c0-6 4-9 9-9s9 3 9 9z"/><path d="M19 2h2v3h3v2h-3v3h-2V7h-3V5h3z"/></svg>
    <svg class="icon" style="left:736px;top:197px" viewBox="0 0 24 24" fill="none" stroke="var(--white)" stroke-width="2.5"><rect x="2" y="2" width="20" height="20"/><path d="M8 8h8v8"/></svg>
    <svg class="icon" style="left:821px;top:144px" viewBox="0 0 24 24" fill="none" stroke="var(--white)" stroke-width="3"><rect x="2" y="9" width="11" height="6" rx="3" transform="rotate(-45 7.5 12)"/><rect x="11" y="9" width="11" height="6" rx="3" transform="rotate(-45 16.5 12)"/></svg>
    <svg class="icon" style="left:814px;top:398px" viewBox="0 0 24 24" fill="none" stroke="var(--white)" stroke-width="3"><path d="M4 20 20 4M4 4l16 16"/></svg>
    <svg class="icon" style="left:817px;top:539px" viewBox="0 0 24 24" fill="var(--white)"><path d="M2 3h20v14H8l-6 5z"/><circle cx="7" cy="10" r="1.5" fill="var(--navy-mid)"/><circle cx="12" cy="10" r="1.5" fill="var(--navy-mid)"/><circle cx="17" cy="10" r="1.5" fill="var(--navy-mid)"/></svg>
    <svg class="icon" style="left:755px;top:584px" viewBox="0 0 24 24" fill="var(--white)"><path d="M12 3 1 9l11 6 11-6z"/><path d="M5 12v5c3 3 11 3 14 0v-5l-7 4z"/></svg>
    <svg class="icon" style="left:545px;top:582px" viewBox="0 0 24 24" fill="var(--orange)"><circle cx="5" cy="19" r="3"/><path d="M2 10a12 12 0 0 1 12 12h-3a9 9 0 0 0-9-9zM2 3a19 19 0 0 1 19 19h-3A16 16 0 0 0 2 6z"/></svg>
    <svg class="icon" style="left:421px;top:626px" viewBox="0 0 24 24" fill="var(--magenta)"><rect x="4" y="2" width="3" height="20"/><rect x="10.5" y="2" width="3" height="20"/><rect x="17" y="2" width="3" height="20"/><rect x="2" y="14" width="7" height="4"/><rect x="8.5" y="6" width="7" height="4"/><rect x="15" y="11" width="7" height="4"/></svg>
    <svg class="icon" style="left:484px;top:883px" viewBox="0 0 24 24" fill="none" stroke="var(--white)" stroke-width="2"><circle cx="12" cy="12" r="10"/><ellipse cx="12" cy="12" rx="4" ry="10"/><path d="M2 12h20"/></svg>
    <svg class="icon" style="left:152px;top:569px" viewBox="0 0 24 24" fill="none" stroke="var(--white)" stroke-width="2.5"><path d="M4 20 6 14 17 3l4 4-11 11z"/><path d="M14 6l4 4"/></svg>
  </section>

  <footer class="footer">
    <div class="brand brand--reef"><span class="brand__dot"></span>Reefhouse</div>
    <div class="brand brand--study">StudyScale</div>
    <div class="brand brand--skill">Skillforge</div>
    <div class="brand brand--kvr">KVR</div>
    <div class="brand brand--north">Northwind Trust</div>
  </footer>
</main>
</body>
</html>
```